Harbourline Strategy Group firm

I need a business card that is succint for a Brisbane based business called Harbourline Strategy Group Pty Ltd.
We bridge the gaps between People, Process and Technology.

We are a specialist operational excellence firm, delivering strategic consulting and business advisory services in six core capabilities, across all industries and all business lines to improve performance, efficiency, profitability, automation and scalability, for clients across Australia &New Zealand.
Updates

Hi Designers, I have uploaded the logo in 3D .png format, to assist in card design.

Target Market(s)

Project Management professionals, IT professionals, corporate and government clients managing transitioning or transformation projects.

Contact Information for Business Card

Harbourline Strategy Group Pty Ltd

Daniel Ferreira
Principal Consultant

mobile: +61 417 260 315
email: daniel@harbourlinestrategygroup.com.au
webpage: www.harbourlinestrategygroup.com

professional services: strategic advisors,

Font styles to use
Sans Serif

Requirements
Must have
• Business name: Harbourline Strategy Group
logo: attached
Contact person: Daniel Ferreira
Title: Principal Consultant
contact details:
mobile +61 417 260
email: daniel@HarbourlineStrategyGroup.com.au
website: HarbourlineStrategyGroup.com

on back side with logo include: A.B.N. 58210947362

professional services offered: Business Analysis, Strategic Advisory
Nice to have
• QR code
Should not have
• contacts picture

```html
<!DOCTYPE html>
<html lang="en">
<head>
<meta charset="utf-8">
<title>Harbourline Strategy Group – Business Card</title>
<link href="https://fonts.googleapis.com/css2?family=Lato:wght@400;700;900&display=swap" rel="stylesheet">
<style>
  :root {
    --navy: #22284a;
    --red: #e0232b;
    --white: #ffffff;
    --ink: #2b2f45;
    --bg: #e9eaee;
  }
  * { margin: 0; padding: 0; box-sizing: border-box; }
  html, body { width: 1200px; height: 900px; overflow: hidden; }
  body {
    background: var(--bg);
    font-family: 'Lato', sans-serif;
    display: flex;
    align-items: center;
    justify-content: center;
    gap: 40px;
  }
  .card {
    position: relative;
    width: 560px;
    height: 320px;
    overflow: hidden;
    box-shadow: 0 6px 18px rgba(0,0,0,0.15);
  }
  .card--front { background: var(--white); }
  .card--back { background: var(--navy); }

  /* Wordmark */
  .wordmark {
    position: absolute;
    display: flex;
    align-items: center;
    gap: 10px;
    font-weight: 900;
    text-transform: uppercase;
    line-height: 1.05;
  }
  .wordmark__dot { flex: none; border-radius: 50%; background: var(--red); }
  .card--front .wordmark { left: 34px; top: 70px; color: var(--navy); font-size: 21px; width: 230px; }
  .card--front .wordmark__dot { width: 18px; height: 18px; }
  .card--back .wordmark { left: 0; right: 0; top: 100px; justify-content: center; color: var(--white); font-size: 34px; }
  .card--back .wordmark__dot { width: 26px; height: 26px; }
  .wordmark__suffix { display: block; font-size: 9px; font-weight: 700; letter-spacing: 1px; margin-top: 4px; }
  .card--back .wordmark__suffix { font-size: 11px; }

  /* Divider */
  .divider {
    position: absolute;
    left: 286px; top: 96px;
    width: 1px; height: 102px;
    background: var(--red);
  }

  /* Contact block */
  .contact { position: absolute; left: 306px; top: 96px; color: var(--ink); }
  .contact__name { color: var(--red); font-weight: 900; font-size: 22px; }
  .contact__title { font-size: 13px; margin: 2px 0 12px; }
  .contact__list { list-style: none; font-size: 12px; }
  .contact__list li { display: flex; align-items: center; gap: 7px; margin-bottom: 4px; }
  .contact__icon { width: 11px; height: 11px; flex: none; }

  /* Bottom tabs */
  .tab {
    position: absolute;
    left: -2px; bottom: -2px;
    width: 240px; height: 52px;
  }
  .tab svg { position: absolute; inset: 0; }
  .tab__text {
    position: relative;
    display: flex; align-items: center;
    height: 100%;
    padding-left: 26px; padding-top: 6px;
    font-size: 14px;
    letter-spacing: 1.5px;
  }
  .card--front .tab__text { color: var(--white); }
  .card--back .tab { width: 300px; }
  .card--back .tab__text { color: var(--navy); font-size: 13px; letter-spacing: 0.3px; }
</style>
</head>
<body>

<section class="card card--front" aria-label="Business card front">
  <div class="wordmark">
    <span class="wordmark__dot"></span>
    <span>Harbourline Strategy Group<span class="wordmark__suffix">Pty Ltd</span></span>
  </div>

  <div class="divider"></div>

  <div class="contact">
    <p class="contact__name">Daniel Ferreira</p>
    <p class="contact__title">Principal Consultant</p>
    <ul class="contact__list">
      <li>
        <svg class="contact__icon" viewBox="0 0 12 12"><path d="M2.5 1 L4.5 1 L5.3 3.6 L4 4.6 Q5 7 7.4 8 L8.4 6.7 L11 7.5 L11 9.5 Q10.5 11 9 11 Q1 10 1 3 Q1 1.5 2.5 1Z" fill="var(--red)"/></svg>
        +61 417 260 315
      </li>
      <li>
        <svg class="contact__icon" viewBox="0 0 12 12"><rect x="0.5" y="2" width="11" height="8" fill="var(--red)"/><path d="M0.5 2 L6 6.5 L11.5 2" fill="none" stroke="#fff" stroke-width="1"/></svg>
        daniel@harbourlinestrategygroup.com.au
      </li>
      <li>
        <svg class="contact__icon" viewBox="0 0 12 12"><circle cx="6" cy="6" r="5" fill="none" stroke="var(--red)" stroke-width="1.2"/><path d="M1 6 H11 M6 1 Q3 6 6 11 M6 1 Q9 6 6 11" fill="none" stroke="var(--red)" stroke-width="0.9"/></svg>
        www.harbourlinestrategygroup.com
      </li>
    </ul>
  </div>

  <div class="tab">
    <svg viewBox="0 0 240 52" preserveAspectRatio="none" aria-hidden="true">
      <path d="M0 52 L0 10 L176 10 Q190 10 196 22 L212 44 Q218 52 240 52 Z" fill="var(--navy)" stroke="var(--red)" stroke-width="2"/>
    </svg>
    <p class="tab__text">A.B.N. 58210947362</p>
  </div>
</section>

<section class="card card--back" aria-label="Business card back">
  <div class="wordmark">
    <span class="wordmark__dot"></span>
    <span>Harbourline<br>Strategy Group<span class="wordmark__suffix">Pty Ltd</span></span>
  </div>

  <div class="tab">
    <svg viewBox="0 0 300 52" preserveAspectRatio="none" aria-hidden="true">
      <path d="M0 52 L0 10 L236 10 Q250 10 256 22 L272 44 Q278 52 300 52 Z" fill="var(--white)" stroke="var(--red)" stroke-width="2"/>
    </svg>
    <p class="tab__text">Business Analysis, Strategic Advisory</p>
  </div>
</section>

</body>
</html>
```